Window and GutterCleaning Flyer A5 size double sided.

We need a double sided A5 flyer. Side 1, is for window cleaning, side 2 is for gutter cleaning. Licensed by Borough of Halvern Council.
Phone number 0800 315 4720.
Business address 7 Tarnlow Brae, North Pellin Edinburgh EH14 3RW.
www.clearpane-vista-services.com
We use a LoftPro Gutter inspection Cam to view your gutters first to see if they need doing.
Window cleaning ; Professional window cleaning services, what we offer, water fed pole window cleaning able to reach windows up to 60 feet.
Conservatory cleaning.
Conservatory roof cleaning.
Fascias & Soffits cleaning.
Excellent Customer Service.
Target Market(s)
domestic houses
Industry/Entity Type
window cleaning
Look and feel
Each slider illustrates characteristics of the customer's brand and the style your logo design should communicate.

```html
<!DOCTYPE html>
<html lang="en">
<head>
<meta charset="utf-8">
<title>ClearPane Vista – Window &amp; Gutter Cleaning Flyer</title>
<link rel="stylesheet" href="https://fonts.googleapis.com/css2?family=Roboto+Condensed:wght@700&family=Roboto:wght@300;400;700&display=swap">
<style>
  :root {
    --backdrop: #cfcfcf;
    --navy: #28275c;
    --sky: #a3c9ea;
    --paper: #ffffff;
    --ink: #1d1d2b;
    --photo-light: #e9edf0;
    --photo-mid: #b9c3cb;
    --photo-dark: #5f6570;
    --autumn: #b07a3c;
    --roof: #3b3f46;
  }
  * { box-sizing: border-box; margin: 0; padding: 0; }
  html, body {
    width: 1200px; height: 2351px; overflow: hidden;
    background: var(--backdrop);
    font-family: "Roboto", Arial, sans-serif;
  }
  .flyer {
    position: absolute; left: 230px; width: 741px; height: 1045px;
    background: var(--paper); overflow: hidden;
    box-shadow: 8px 10px 14px rgba(0,0,0,.35);
  }
  .flyer--window { top: 78px; }
  .flyer--gutter { top: 1201px; }
  .flyer__art { position: absolute; inset: 0; width: 741px; height: 1045px; }
  .headline {
    position: absolute; right: 62px;
    font-family: "Roboto Condensed", "Arial Narrow", sans-serif;
    font-weight: 700; font-size: 80px; line-height: 70px;
    color: var(--paper); text-align: right;
    text-shadow: 3px 4px 6px rgba(0,0,0,.55);
  }
  .flyer--window .headline { top: 352px; }
  .flyer--gutter .headline { top: 112px; }
  .brand {
    position: absolute;
    font-family: "Roboto", Arial, sans-serif; font-weight: 700;
    color: var(--navy); line-height: 1;
  }
  .flyer--window .brand { left: 61px; top: 120px; font-size: 44px; width: 200px; }
  .flyer--gutter .brand { left: 556px; top: 920px; font-size: 28px; width: 140px; text-align: center; }
  .copy {
    position: absolute; left: 61px;
    font-size: 16px; line-height: 21.2px; font-weight: 300;
  }
  .copy p + p { margin-top: 21px; }
  .flyer--window .copy { top: 528px; color: var(--paper); }
  .flyer--gutter .copy { top: 293px; color: var(--ink); }
  .contact {
    position: absolute; left: 61px; top: 896px;
    font-size: 16px; line-height: 21.2px; font-weight: 300;
    list-style: none;
  }
  .flyer--window .contact { color: var(--paper); }
  .flyer--gutter .contact { color: var(--ink); }
  .contact li { position: relative; padding-left: 26px; }
  .contact li.contact__web { margin-top: 22px; }
  .contact svg { position: absolute; left: 0; top: 5px; width: 11px; height: 11px; }
</style>
</head>
<body>

<section class="flyer flyer--window">
  <svg class="flyer__art" viewBox="0 0 741 1045">
    <defs>
      <linearGradient id="windowPhotoTone" x1="0" y1="0" x2="1" y2="1">
        <stop offset="0" stop-color="var(--photo-light)"/>
        <stop offset=".45" stop-color="var(--photo-mid)"/>
        <stop offset=".75" stop-color="var(--photo-dark)"/>
        <stop offset="1" stop-color="var(--photo-mid)"/>
      </linearGradient>
    </defs>
    <rect x="0" y="0" width="741" height="1045" fill="url(#windowPhotoTone)" role="img" aria-label="Photo: window cleaner in gloves wiping a tall apartment window with a squeegee pole, city view behind"/>
    <polygon points="0,0 8,0 201,335 0,410" fill="var(--paper)"/>
    <polygon points="0,410 201,335 595,1045 0,1045" fill="var(--navy)"/>
  </svg>
  <div class="brand">ClearPane Vista</div>
  <h1 class="headline">WINDOW<br>CLEANING</h1>
  <div class="copy">
    <p>We offer a high quality,<br>professional window cleaning<br>service across west Edinburgh.<br>Licensed by Borough of<br>Halvern Council.</p>
    <p>Regular window cleaning helps to<br>avoid the build-up of dirt and residue<br>on the glass, letting more light into<br>your home. Our water fed pole system<br>reaches windows up to 60 feet. We also<br>offer conservatory and conservatory roof<br>cleaning, fascias &amp; soffits cleaning,<br>gutter/rhone cleaning and builders cleans,<br>all backed by excellent customer service.</p>
  </div>
  <ul class="contact">
    <li><svg viewBox="0 0 12 12"><path d="M2 1l2.5 0 1 3-1.5 1c.7 1.4 1.6 2.3 3 3l1-1.5 3 1V11c-5 0-9-4-9-9z" fill="currentColor"/></svg>0800 315 4720</li>
    <li><svg viewBox="0 0 12 12"><path d="M6 0a4 4 0 0 1 4 4c0 3-4 8-4 8S2 7 2 4a4 4 0 0 1 4-4zm0 2.5a1.5 1.5 0 1 0 0 3 1.5 1.5 0 0 0 0-3z" fill="currentColor"/></svg>7 Tarnlow Brae<br>&nbsp;North Pellin Edinburgh EH14 3RW</li>
    <li class="contact__web"><svg viewBox="0 0 12 12"><circle cx="6" cy="6" r="5" fill="none" stroke="currentColor" stroke-width="1.6"/><path d="M1 6h10M6 1v10" stroke="currentColor" stroke-width="1"/></svg>www.clearpane-vista-services.com</li>
  </ul>
</section>

<section class="flyer flyer--gutter">
  <svg class="flyer__art" viewBox="0 0 741 1045">
    <defs>
      <linearGradient id="gutterPhotoTone" x1="0" y1="0" x2="1" y2="1">
        <stop offset="0" stop-color="var(--roof)"/>
        <stop offset=".5" stop-color="#6b5a45"/>
        <stop offset="1" stop-color="var(--autumn)"/>
      </linearGradient>
    </defs>
    <rect x="0" y="0" width="741" height="552" fill="url(#gutterPhotoTone)" role="img" aria-label="Photo: gloved hand clearing autumn leaves from a roof gutter, trees in the background"/>
    <polygon points="0,0 195,180 0,243" fill="var(--paper)"/>
    <polygon points="0,243 195,180 658,551 741,551 741,711 651,864 389,864 535,1045 0,1045" fill="var(--sky)"/>
    <polygon points="389,864 425,864 571,1045 535,1045" fill="var(--navy)"/>
  </svg>
  <h1 class="headline">GUTTER<br>CLEANING</h1>
  <div class="copy">
    <p>ClearPane Vista offer a<br>fast and easy gutter cleaning<br>service on residential and commercial<br>properties.</p>
    <p>Gutters are an important part of your home.<br>Letting your gutters get blocked up can cause<br>damage to your property, so why not set up an annual<br>plan and make sure you don’t run into problems when<br>winter comes.</p>
    <p>Over time your gutters will fill up with moss, leaves and other<br>unwanted debris which will affect the appearance of your home.<br>When gutters aren’t cleared and emptied on a regular basis they become heavy<br>and risk pulling away from the fascias.</p>
    <p>When gutters are not clear it can also lead to blockages in the gutters and<br>downpipes, which will cause the water to overflow. The water which overflows from<br>the guttering can lead to damp problems and other problems in the structure of<br>your property which can become a costly repair.</p>
    <p>We recommend gutters to be cleared out once a year. We use a LoftPro gutter<br>inspection cam to view your gutters first and see if they need doing. If they are<br>blocked, contact us for a free no obligation quote to clear them out and get them<br>working as they should. With our gutter cleaning service we will clear all gutters<br>and unblock all downpipes ensuring the water is running freely and down your drains.</p>
  </div>
  <ul class="contact">
    <li><svg viewBox="0 0 12 12"><path d="M2 1l2.5 0 1 3-1.5 1c.7 1.4 1.6 2.3 3 3l1-1.5 3 1V11c-5 0-9-4-9-9z" fill="currentColor"/></svg>0800 315 4720</li>
    <li><svg viewBox="0 0 12 12"><path d="M6 0a4 4 0 0 1 4 4c0 3-4 8-4 8S2 7 2 4a4 4 0 0 1 4-4zm0 2.5a1.5 1.5 0 1 0 0 3 1.5 1.5 0 0 0 0-3z" fill="currentColor"/></svg>7 Tarnlow Brae<br>&nbsp;North Pellin Edinburgh EH14 3RW</li>
    <li class="contact__web"><svg viewBox="0 0 12 12"><circle cx="6" cy="6" r="5" fill="none" stroke="currentColor" stroke-width="1.6"/><path d="M1 6h10M6 1v10" stroke="currentColor" stroke-width="1"/></svg>www.clearpane-vista-services.com</li>
  </ul>
  <div class="brand">ClearPane Vista</div>
</section>

</body>
</html>
```